Criação de Kit com 5 Layouts de Post para Redes Sociais (Facebook, Instagram e etc) para Consultoria de Negócios
" EVENTO DE DOIS DIAS COM VÁRIOS PALESTRANTES, TRAZENDO CONHECIMENTO EM VARIAS ÁREAS PARA AS MULHERES EMPREENDEDORAS. UM EVENTO DE IMERSSAO DE 19 HORAS. "

```html
<!DOCTYPE html>
<html lang="pt-BR">
<head>
<meta charset="UTF-8">
<title>VELA — Para a Mulher Contemporânea</title>
<link href="https://fonts.googleapis.com/css2?family=Josefin+Sans:wght@400;600;700&family=Cormorant+Garamond:wght@500&display=swap" rel="stylesheet">
<style>
  :root {
    --plum: #4a1331;
    --plum-deep: #3d0f28;
    --gold: #d4a63c;
    --gold-light: #e8c777;
    --paper: #f3f3f4;
    --paper-shade: #e4e4e7;
    --white: #ffffff;
  }
  * { margin: 0; padding: 0; box-sizing: border-box; }
  html, body { width: 1200px; height: 1200px; overflow: hidden; }
  body { background: var(--paper); font-family: 'Josefin Sans', sans-serif; }
  .post { position: relative; width: 1200px; height: 1200px; overflow: hidden; }

  .photo-area {
    position: absolute; inset: 0;
    background:
      radial-gradient(ellipse 420px 620px at 330px 470px, rgba(196,168,150,0.55), rgba(196,168,150,0) 70%),
      radial-gradient(ellipse 300px 380px at 360px 700px, rgba(150,170,205,0.45), rgba(150,170,205,0) 70%),
      linear-gradient(180deg, var(--paper) 0%, var(--paper-shade) 100%);
  }

  .headline {
    position: absolute; left: 708px; top: 112px;
    color: var(--plum);
    font-weight: 700; font-size: 86px; line-height: 82px;
    letter-spacing: 5px; text-transform: uppercase;
  }
  .headline-rule {
    position: absolute; left: 984px; top: 484px;
    width: 110px; height: 6px; background: var(--gold);
  }

  .footer-band { position: absolute; left: 0; top: 0; width: 1200px; height: 1200px; }

  .brand { position: absolute; left: 60px; top: 972px; display: flex; align-items: center; }
  .brand-mark {
    width: 150px; height: 150px; border-radius: 50%;
    border: 4px solid var(--gold); flex-shrink: 0;
  }
  .brand-text { margin-left: 30px; color: var(--white); }
  .brand-name {
    font-family: 'Cormorant Garamond', serif; font-weight: 500;
    font-size: 112px; line-height: 96px; letter-spacing: 4px;
  }
  .brand-tagline {
    font-family: 'Cormorant Garamond', serif; font-weight: 500;
    font-size: 21px; line-height: 22px; letter-spacing: 1px;
    text-transform: uppercase; margin-top: 8px;
  }

  .contact { position: absolute; left: 612px; top: 1070px; color: var(--white); }
  .contact-label { font-size: 26px; font-weight: 600; letter-spacing: 1px; }
  .contact-list { display: flex; gap: 40px; margin-top: 14px; list-style: none; }
  .contact-item { display: flex; align-items: center; gap: 12px; font-size: 26px; }
  .contact-icon { width: 30px; height: 30px; }
</style>
</head>
<body>
<main class="post">
  <div class="photo-area" role="img" aria-label="Fotografia de uma mulher sorridente com camisa listrada azul e branca, estendendo a mão aberta para a direita, sobre fundo claro"></div>

  <h1 class="headline">Para a<br>Mulher<br>Contem<br>porânea</h1>
  <div class="headline-rule"></div>

  <svg class="footer-band" viewBox="0 0 1200 1200" aria-hidden="true">
    <path d="M0 820 C 250 770, 600 840, 900 940 C 1010 975, 1110 985, 1200 980 L1200 1200 L0 1200 Z" fill="var(--plum)"/>
    <path d="M0 808 C 300 760, 640 830, 1000 1000 C 720 870, 340 790, 0 836 Z" fill="var(--gold)"/>
  </svg>

  <div class="brand">
    <div class="brand-mark"></div>
    <div class="brand-text">
      <div class="brand-name">VELA</div>
      <div class="brand-tagline">Encontro de Negócios<br>&amp; Liderança Feminina</div>
    </div>
  </div>

  <div class="contact">
    <p class="contact-label">CONTATO:</p>
    <ul class="contact-list">
      <li class="contact-item">
        <svg class="contact-icon" viewBox="0 0 30 30" aria-hidden="true">
          <circle cx="15" cy="15" r="15" fill="var(--gold)"/>
          <rect x="10" y="7" width="10" height="16" rx="2" fill="none" stroke="var(--plum)" stroke-width="2"/>
          <circle cx="15" cy="20" r="1.2" fill="var(--plum)"/>
        </svg>
        <span>(00) 0000-0000</span>
      </li>
      <li class="contact-item">
        <svg class="contact-icon" viewBox="0 0 30 30" aria-hidden="true">
          <circle cx="15" cy="15" r="15" fill="var(--gold)"/>
          <rect x="8" y="10" width="14" height="10" rx="1" fill="none" stroke="var(--plum)" stroke-width="2"/>
          <path d="M8 10 L15 16 L22 10" fill="none" stroke="var(--plum)" stroke-width="2"/>
        </svg>
        <span>email@email.com.br</span>
      </li>
    </ul>
  </div>
</main>
</body>
</html>
```